Tor'k Wayfarer Travel

We need a sleek, professional, inviting card to elicit global travel for the experienced and professional traveler. Royal blue, black and silver. (perhaps the wording could be silver with black shadow?-get creative) Maybe a watermark on the front and the full raised logo on the back.
We want a stylish and modern card, but professional.

```html
<!DOCTYPE html>
<html lang="en">
<head>
<meta charset="utf-8">
<title>Tor'k Wayfarer Travel – Business Card</title>
<link rel="stylesheet" href="https://fonts.googleapis.com/css2?family=Open+Sans:ital,wght@0,400;0,700;1,400&display=swap">
<style>
  :root {
    --royal-blue: #232e80;
    --card-black: #050505;
    --silver: #d8dbe2;
    --silver-dark: #8d929c;
    --white: #ffffff;
    --sky-blue: #35a5de;
    --backdrop: #e7e7e9;
  }
  * { margin: 0; padding: 0; box-sizing: border-box; }
  html, body {
    width: 1200px;
    height: 960px;
    overflow: hidden;
    background: var(--backdrop);
    font-family: "Open Sans", Arial, sans-serif;
  }
  .card {
    position: absolute;
    left: 250px;
    width: 700px;
    height: 400px;
    background: var(--royal-blue);
    overflow: hidden;
    box-shadow: 0 4px 14px rgba(0,0,0,0.18);
  }
  .card--front { top: 60px; }
  .card--back { top: 510px; }

  .card__band {
    position: absolute;
    inset: 0;
    width: 100%;
    height: 100%;
  }

  .brand-name {
    position: absolute;
    font-weight: 700;
    letter-spacing: 1px;
    text-transform: uppercase;
    text-align: center;
    line-height: 1.1;
  }
  .card--front .brand-name {
    top: 48px;
    left: 250px;
    width: 420px;
    font-size: 30px;
    color: var(--silver);
  }
  .card--back .brand-name {
    top: 150px;
    left: 0;
    width: 100%;
    font-size: 40px;
    color: var(--sky-blue);
  }

  .holder {
    position: absolute;
    top: 188px;
    left: 70px;
    color: var(--white);
    text-align: right;
    width: 250px;
  }
  .holder__name { font-size: 21px; font-weight: 700; }
  .holder__role { font-size: 14px; font-style: italic; margin-top: 4px; }

  .contact {
    position: absolute;
    top: 280px;
    left: 380px;
    list-style: none;
    color: var(--white);
    font-size: 15px;
    line-height: 1.35;
  }
  .contact__item { display: flex; align-items: flex-start; gap: 10px; margin-bottom: 6px; }
  .contact__icon { width: 14px; height: 16px; flex: none; margin-top: 2px; }
</style>
</head>
<body>

<section class="card card--front" aria-label="Business card front">
  <svg class="card__band" viewBox="0 0 700 400" aria-hidden="true">
    <defs>
      <linearGradient id="silverSweep" x1="0" y1="0" x2="1" y2="0">
        <stop offset="0" stop-color="#6f747e"/>
        <stop offset="0.45" stop-color="#f2f3f6"/>
        <stop offset="0.75" stop-color="#9da2ab"/>
        <stop offset="1" stop-color="#e4e6ea"/>
      </linearGradient>
    </defs>
    <path d="M0,148 C160,132 320,128 410,150 C470,166 470,230 540,244 C600,256 660,252 700,250 L700,400 L0,400 Z"
          fill="url(#silverSweep)"/>
    <path d="M0,160 C160,144 310,140 398,162 C455,178 452,246 530,262 C590,274 650,270 700,268 L700,400 L0,400 Z"
          fill="var(--card-black)"/>
  </svg>

  <div class="brand-name">Tor'k Wayfarer<br>Travel</div>

  <div class="holder">
    <p class="holder__name">Marisol Kent Abbott</p>
    <p class="holder__role">Manager</p>
  </div>

  <ul class="contact">
    <li class="contact__item">
      <svg class="contact__icon" viewBox="0 0 14 16" aria-hidden="true">
        <path d="M3 1 L6 1 L7 5 L5 6.5 C6 9 7.5 10.5 9.5 11.5 L11 9.5 L14 10.5 L14 14 C14 15 13 15.5 12 15.3 C6 14 1.5 9 0.8 3 C0.7 2 1.5 1 3 1 Z" fill="var(--white)"/>
      </svg>
      <span>555 010 2468</span>
    </li>
    <li class="contact__item">
      <svg class="contact__icon" viewBox="0 0 14 16" aria-hidden="true">
        <path d="M7 0.5 C3.4 0.5 1 3 1 6 C1 10 7 15.5 7 15.5 C7 15.5 13 10 13 6 C13 3 10.6 0.5 7 0.5 Z M7 8.3 A2.3 2.3 0 1 1 7 3.7 A2.3 2.3 0 1 1 7 8.3 Z" fill="var(--white)"/>
      </svg>
      <span>72 Harlow Ave NE, Denver,<br>CO, 80203</span>
    </li>
  </ul>
</section>

<section class="card card--back" aria-label="Business card back">
  <div class="brand-name">Tor'k Wayfarer<br>Travel</div>
</section>

</body>
</html>
```